Website Online Research Solutions

We are a small European high-tech online research company.
With our own state of the art software we run online panels and are conducting reseach for companies. Partly research via our own panel and partly via panels we maintain for our customers.
Our current website is old and outdatet: www.pravelo.nl.
We are in the process to change the content of the site. We want a modern, european and businesslike design for our new website.
Our logo has to stay the same (left uppersite of our website and attached) but can be changed a little to adapt it to the new design of the website. The colors of the site are up to you.
Target Market(s)
Marketeers and researchers of large and middle size companies in all kind of fields.
Industry/Entity Type
Online
Look and feel
Each slider illustrates characteristics of the customer's brand and the style your logo design should communicate.

```html
<!DOCTYPE html>
<html lang="nl">
<head>
<meta charset="utf-8">
<title>Pravelo – Dataverzameling</title>
<link href="https://fonts.googleapis.com/css2?family=Gelasio:wght@400;500&display=swap" rel="stylesheet">
<style>
  :root {
    --ink: #4a3c3d;
    --text: #4f4446;
    --bar-top: #8d6e70;
    --bar-bottom: #3a2b2c;
    --white: #ffffff;
    --badge-line: #6b5d5e;
    --page: #ffffff;
  }
  * { margin: 0; padding: 0; box-sizing: border-box; }
  html, body { width: 1125px; height: 1200px; overflow: hidden; background: var(--page); }
  body { font-family: "Gelasio", Georgia, serif; color: var(--text); position: relative; }

  .main-nav {
    position: absolute; left: 122px; top: 79px; width: 881px; height: 28px;
    background: linear-gradient(var(--bar-top), var(--bar-bottom));
  }
  .main-nav a, .footer-nav a {
    position: absolute; color: var(--white); text-decoration: none;
    transform: translateX(-50%); white-space: nowrap;
  }
  .main-nav a { top: 5px; font-size: 13px; }
  .main-nav .active::before {
    content: ""; position: absolute; left: -8px; right: -14px; top: -10px; height: 2px;
    background: var(--bar-bottom);
  }
  .main-nav .active::after { content: " ▾"; font-size: 8px; vertical-align: 2px; }

  .brand-badge {
    position: absolute; border-radius: 50%; background: var(--white);
    border: 2px solid var(--badge-line);
    display: flex; align-items: center; justify-content: center;
    color: var(--ink); font-size: 28px; font-weight: 500;
  }
  .brand-badge.header { left: 484px; top: 13px; width: 156px; height: 156px; }
  .brand-badge.footer { left: 122px; top: 998px; width: 94px; height: 94px; font-size: 17px; }

  .section-nav { position: absolute; left: 178px; top: 248px; list-style: none; font-size: 13px; }
  .section-nav li { height: 23.4px; }
  .section-nav li::before { content: "•"; margin-right: 6px; color: var(--ink); }

  h1 { position: absolute; left: 402px; top: 184px; font-size: 41px; font-weight: 400; color: var(--ink); }
  .lead {
    position: absolute; left: 402px; top: 259px; width: 560px;
    font-size: 24px; line-height: 28px; color: var(--ink);
  }
  h2 { position: absolute; left: 402px; top: 664px; font-size: 26px; font-weight: 400; color: var(--ink); }

  .body-text { position: absolute; left: 405px; width: 535px; font-size: 12.7px; line-height: 23.4px; }
  .body-text p + p { margin-top: 23.4px; }
  .body-text.first { top: 427px; }
  .body-text.second { top: 708px; }

  .visual { position: absolute; left: 178px; width: 206px; }
  .visual.collection { top: 433px; height: 147px; background: linear-gradient(160deg, #eef3f5, #b7c2c8); }
  .visual.streaming { top: 712px; height: 233px; background: linear-gradient(#3f7fa0 0%, #9fc0d0 40%, #eef1f3 55%, #dfe5e8 100%); }

  .site-footer {
    position: absolute; left: 0; top: 1031px; width: 1125px; height: 169px;
    background: linear-gradient(var(--bar-top), var(--bar-bottom));
  }
  .footer-nav a { top: 27px; font-size: 13px; }
  .legal {
    position: absolute; left: 291px; top: 75px; width: 708px;
    color: var(--white); font-size: 9.8px; line-height: 14px;
  }
</style>
</head>
<body>
  <nav class="main-nav">
    <a href="#" style="left:59px">Algemeen</a>
    <a href="#" class="active" style="left:187px">Producten</a>
    <a href="#" style="left:305px">Demo’s</a>
    <a href="#" style="left:577px">Referenties</a>
    <a href="#" style="left:700px">Personeel</a>
    <a href="#" style="left:822px">Contact</a>
  </nav>
  <div class="brand-badge header">Pravelo</div>

  <ul class="section-nav">
    <li>Dataverzameling</li>
    <li>Analyse</li>
    <li>Klanten</li>
    <li>Dataset publishing</li>
    <li>Panel: inPeilo</li>
  </ul>

  <h1>Dataverzameling</h1>
  <p class="lead">Vragenlijsten die door Pravelo worden geprogrammeerd zijn dynamisch gegenereerde vragenlijsten die in de “look &amp; feel” worden geprogrammeerd van onze klanten en/of de produkten van onze klanten.</p>

  <div class="visual collection" role="img" aria-label="Illustratie van mensen op een kaart van Europa met antwoorden die worden opgezogen"></div>
  <div class="body-text first">
    <p>Pravelo programmeert vragenlijsten/enquetes voor gegevensverzameling via internet, intranet of via email. Recentelijk hebben we zelfs betrouwbare methoden ontwikkeld voor onderzoek via SMS.</p>
    <p>De vele honderden onderzoeken die wij hebben geprogrammeerd varieren van eenvoudige onderzoeken via quickpolls met een aantal korte stellingen of banners tot en met complexe (inter)nationale multilinguale monitoren, medewerker&amp;klanttevredenheid onderzoek, usability tests etc.</p>
  </div>

  <h2>Streaming audio/video</h2>
  <div class="visual streaming" role="img" aria-label="Illustratie van een videospeler met een online vraag over een commercial"></div>
  <div class="body-text second">
    <p>Daarnaast hebben we betrouwbare en eenvoudige technieken ontwikkeld voor online onderzoek ten behoeve van pre-testing van radio&amp;TV commercials waarbij gebruik gemaakt wordt van streaming audio/video.&nbsp; Pravelo stelt haar opdrachtgevers vervolgens in staat om op eenvoudige wijze de verzamelde onderzoeksgegevens online te bekijken en deze eveneens online te analyseren via een online analysetool.</p>
    <p>Doordat deze analyse- tool zeer gebruikers- vriendelijk werd ontworpen is deze niet alleen geschikt voor opinieonder- zoekbureau’s maar ook voor bedrijven met een eigen researchafdeling en/of ervaren opinieonderzoekers.</p>
  </div>

  <footer class="site-footer">
    <nav class="footer-nav">
      <a href="#" style="left:321px">Algemeen</a>
      <a href="#" style="left:418px">Producten</a>
      <a href="#" style="left:513px">Demo’s</a>
      <a href="#" style="left:609px">Referenties</a>
      <a href="#" style="left:705px">Personeel</a>
      <a href="#" style="left:800px">Contact</a>
    </nav>
    <p class="legal">(c) 2010 Pravelo. Lorem ipsum dolor sit amet, consectetuer adipiscing elit, sed diam nonummy nibh euismod tincidunt ut laoreet dolore magna aliquam erat volutpat. Ut wisi enim ad minim veniam, quis nostrud exerci tation ullamcorper suscipit lobortis nisl ut aliquip ex ea commodo consequat. Duis autem vel eum iriure dolor in hendrerit in vulputate velit esse molestie consequat, vel illum dolore eu feugiat nulla facilisis at vero eros et accumsan et iusto odio dignissim qui blandit praesent luptatum zzril delenit augue duis dolore te feugait nulla facilisi.</p>
  </footer>
  <div class="brand-badge footer">Pravelo</div>
</body>
</html>
```